Female Pest Controller needs awesome business cards

I need a logo design for a Pest Control service - something that appeals to 'nature' & safe, with the use of the colour green. I am also female
New Business Name is 'Bug Begone Bay'
appeals to women

Target Market(s)

Domestic Households & Local Businesses

Industry/Entity Type

Pest Control

Contact Information for Business Card

Corinne Waldrake
0428316952
ABN 47 618 259 304
PMT7314958207
Spiders Cockroaches, Ants, Silverfish, Fleas, Rodents

Font styles to use
Decorative

Colors
abd036
aaaaaa
5c5c5c

Requirements
Should not have
• Pics of dead insects, prefer nature inspired designs, frogs, trees etc
• Have attached old log & business name ( now my ex's business) Bug Begone Bay -

```html
<!DOCTYPE html>
<html lang="en">
<head>
<meta charset="utf-8">
<title>Bug Begone Bay – Business Card</title>
<link href="https://fonts.googleapis.com/css2?family=Arimo:wght@400;700&display=swap" rel="stylesheet">
<style>
  :root {
    --lime: #abd036;
    --lime-soft: #b9d85a;
    --lime-faint: #eef4dc;
    --grey-light: #aaaaaa;
    --grey-dark: #5c5c5c;
    --ink: #333333;
    --paper: #ffffff;
    --backdrop: #26272b;
  }
  * { margin: 0; padding: 0; box-sizing: border-box; }
  html, body { width: 1200px; height: 800px; overflow: hidden; }
  body {
    background: var(--backdrop);
    font-family: "Arimo", Arial, sans-serif;
    position: relative;
  }
  .card {
    position: absolute;
    width: 520px;
    height: 300px;
    overflow: hidden;
    box-shadow: 0 12px 30px rgba(0,0,0,.45);
  }

  /* Back of card */
  .card-back { left: 70px; top: 90px; background: var(--lime); }
  .card-back .pattern-area {
    position: absolute; inset: 0;
    background: radial-gradient(circle at 40% 45%, var(--lime-soft), var(--lime) 75%);
  }
  .card-back .brand {
    position: absolute; right: 26px; bottom: 26px;
    display: flex; align-items: center; gap: 8px;
    color: var(--paper); font-weight: 700; font-size: 18px;
  }
  .brand-dot { width: 14px; height: 14px; border-radius: 50%; background: var(--paper); flex: none; }

  /* Front of card */
  .card-front { left: 610px; top: 400px; background: var(--paper); }
  .front-band { position: absolute; inset: 0; }
  .front-brand {
    position: absolute; left: 28px; top: 34px;
    display: flex; align-items: center; gap: 10px;
    color: var(--grey-dark); font-weight: 700; font-size: 30px; letter-spacing: -0.5px;
  }
  .front-brand .brand-dot { width: 22px; height: 22px; background: var(--lime); }

  .holder { position: absolute; left: 150px; top: 128px; }
  .holder-name { font-weight: 700; font-size: 15px; color: var(--grey-dark); letter-spacing: .3px; }
  .holder-role { font-size: 12px; color: var(--lime); margin-top: 2px; }
  .holder-rule { width: 170px; height: 1px; background: var(--lime); margin: 8px 0; }
  .contact-list { list-style: none; }
  .contact-list li {
    display: flex; align-items: center; gap: 6px;
    font-size: 11px; color: var(--ink); line-height: 17px;
  }
  .contact-list .accent { color: var(--lime); }
  .contact-icon { width: 13px; height: 13px; flex: none; }

  .company-divider {
    position: absolute; right: 24px; top: 112px;
    width: 150px; height: 1px; background: var(--lime);
  }
  .company {
    position: absolute; right: 24px; top: 120px; text-align: right;
    font-style: normal; font-size: 11px; color: var(--ink); line-height: 15px;
  }
</style>
</head>
<body>

<section class="card card-back" aria-label="Card back">
  <div class="pattern-area" role="img" aria-label="Repeating brand pattern in soft green tones"></div>
  <div class="brand"><span class="brand-dot"></span>Bug Begone Bay</div>
</section>

<section class="card card-front" aria-label="Card front">
  <svg class="front-band" width="520" height="300" viewBox="0 0 520 300" aria-hidden="true">
    <polygon points="0,118 0,300 190,300" fill="var(--lime)"/>
    <line x1="0" y1="106" x2="205" y2="300" stroke="var(--grey-dark)" stroke-width="3"/>
  </svg>

  <div class="front-brand"><span class="brand-dot"></span>Bug Begone Bay</div>

  <div class="holder">
    <div class="holder-name">CORINNE WALDRAKE</div>
    <div class="holder-role">Founder</div>
    <div class="holder-rule"></div>
    <ul class="contact-list">
      <li>
        <svg class="contact-icon" viewBox="0 0 14 14" aria-hidden="true"><circle cx="7" cy="7" r="7" fill="var(--lime)"/><path d="M4.5 3.5h1.5l.6 2-1 .8a5 5 0 0 0 2.1 2.1l.8-1 2 .6v1.5a1 1 0 0 1-1 1A6 6 0 0 1 3.5 4.5a1 1 0 0 1 1-1z" fill="#fff"/></svg>
        +61 428 316 952
      </li>
      <li>
        <svg class="contact-icon" viewBox="0 0 14 14" aria-hidden="true"><circle cx="7" cy="7" r="7" fill="var(--lime)"/><rect x="3.5" y="4.5" width="7" height="5" fill="#fff"/><path d="M3.5 4.5 7 7.3l3.5-2.8" fill="none" stroke="var(--lime)" stroke-width=".8"/></svg>
        hello@bugbegonebay.com.au
      </li>
      <li>
        <svg class="contact-icon" viewBox="0 0 14 14" aria-hidden="true"><circle cx="7" cy="7" r="7" fill="var(--lime)"/><circle cx="7" cy="7" r="3.6" fill="none" stroke="#fff" stroke-width=".9"/><path d="M3.4 7h7.2M7 3.4c-1.6 2-1.6 5.2 0 7.2M7 3.4c1.6 2 1.6 5.2 0 7.2" fill="none" stroke="#fff" stroke-width=".8"/></svg>
        <span>www.<span class="accent">bugbegonebay</span>.com.au</span>
      </li>
    </ul>
  </div>

  <div class="company-divider"></div>
  <address class="company">
    Bug Begone Bay<br>
    ABN 47 618 259 304<br>
    PMT7314958207
  </address>
</section>

</body>
</html>
```